Bricks in the Wall

We need graphics for a 5x7 or 6x9 post card, single sided for a small speech language pathology practice that serves pediatric patients primarily with children on the autism spectrum.

I want a brick wall, with words and phrases written into the bricks. (to follow)
A child standing on top of the wall with hands up in success.
A few incomplete autism puzzles on the ground.
A larger complete autism puzzle in the the child's hand.
The title is: Speech/Language Therapy
The Foundation for Communication Success
Words/phrases to go into the red bricks:
Receptive Language, Expressive Language, Pragmatics, Sensory, cognitive,
social language, autism, articulation, TeleTherapy, auditory processing, screening, evaluation, developmental delay, Goals, family involvement, environmental communication, ASD, Mirror Neurons.

Target Market(s)

Children with speech and language disorders.

Industry/Entity Type

Speech and Language Therapy

Font styles to use
Serif

Requirements
Must have
• Colors, primary and red bricks.
Nice to have
• I want the postcard to have a happy feel to it and a sense of success.
Should not have
• I don't want it cluttered.

```html
<!DOCTYPE html>
<html lang="en">
<head>
<meta charset="utf-8">
<title>Speech/Language Therapy – The Foundation for Communication Success</title>
<link rel="stylesheet" href="https://fonts.googleapis.com/css2?family=Alfa+Slab+One&family=Patua+One&display=swap">
<style>
  :root{
    --sky-top:#7fd3e8;
    --sky-bottom:#6fc2e0;
    --title-ink:#4a4fa3;
    --headline-white:#ffffff;
    --mortar:#9c4a22;
    --brick-a:#c8652b;
    --brick-b:#b9572a;
    --brick-c:#c97a2e;
    --brick-d:#c15e2a;
    --word-ink:#ffffff;
    --grass:#6cb33f;
    --grass-dark:#4f9a2c;
  }
  html,body{margin:0;padding:0;overflow:hidden;background:#ffffff;}
  .postcard{position:relative;width:1200px;height:849px;overflow:hidden;
    background:linear-gradient(180deg,var(--sky-top),var(--sky-bottom));}
  .wall{position:absolute;left:0;top:0;width:1200px;height:849px;}
  .brick-a{fill:var(--brick-a);}
  .brick-b{fill:var(--brick-b);}
  .brick-c{fill:var(--brick-c);}
  .brick-d{fill:var(--brick-d);}
  .mortar{fill:var(--mortar);}
  .cloud{fill:#ffffff;}
  .ground{fill:var(--grass);}
  .ground-edge{fill:var(--grass-dark);}

  .child-art{position:absolute;left:120px;top:28px;width:180px;height:224px;border-radius:24px 24px 6px 6px;
    background:linear-gradient(180deg,#f2d31e 0%,#e55a9c 16%,#e2473f 30%,#f2d57a 46%,#2d8a86 72%,#1f6e6a 100%);opacity:.85;}
  .ground-puzzle{position:absolute;top:806px;height:38px;border-radius:10px;opacity:.9;}
  .ground-puzzle.left{left:30px;width:170px;background:linear-gradient(90deg,#3c8fcf,#7cc35a);}
  .ground-puzzle.right{left:990px;width:180px;background:linear-gradient(90deg,#f2d31e,#e55a9c);}

  .masthead{position:absolute;left:320px;top:12px;width:860px;margin:0;text-align:center;}
  .title{margin:0;font-family:"Patua One",serif;font-weight:400;font-size:56px;line-height:1;
    color:var(--title-ink);white-space:nowrap;}
  .subtitle{margin:8px 0 0;font-family:"Patua One",serif;font-weight:400;font-size:30px;line-height:1;
    color:var(--title-ink);white-space:nowrap;}
  .headline{margin:6px 0 0;font-family:"Alfa Slab One",serif;font-weight:400;font-size:104px;line-height:1;
    color:var(--headline-white);letter-spacing:3px;
    text-shadow:5px 6px 0 var(--title-ink);-webkit-text-stroke:2px var(--title-ink);}

  .brick-word{position:absolute;margin:0;display:flex;align-items:center;justify-content:center;
    text-align:center;font-family:"Patua One",serif;font-weight:400;font-size:26px;line-height:1.1;
    color:var(--word-ink);text-shadow:1px 2px 0 rgba(90,40,15,.35);box-sizing:border-box;padding:0 8px;}
</style>
</head>
<body>
<div class="postcard">
  <svg class="wall" viewBox="0 0 1200 849" aria-hidden="true">
    <g>
      <circle class="cloud" cx="1185" cy="215" r="40"/>
      <circle class="cloud" cx="1145" cy="238" r="22"/>
      <circle class="cloud" cx="1118" cy="248" r="14"/>
      <rect class="cloud" x="1090" y="240" width="110" height="14"/>
    </g>
    <rect class="mortar" x="0" y="252" width="1200" height="548"/>
    <g>
      <rect class="brick-b" x="0" y="252" width="218" height="78"/>
      <rect class="brick-a" x="224" y="252" width="244" height="78"/>
      <rect class="brick-c" x="474" y="252" width="243" height="78"/>
      <rect class="brick-a" x="723" y="252" width="247" height="78"/>
      <rect class="brick-d" x="976" y="252" width="224" height="78"/>

      <rect class="brick-a" x="0" y="336" width="97" height="83"/>
      <rect class="brick-a" x="103" y="336" width="244" height="83"/>
      <rect class="brick-d" x="353" y="336" width="247" height="83"/>
      <rect class="brick-a" x="606" y="336" width="243" height="83"/>
      <rect class="brick-a" x="855" y="336" width="244" height="83"/>
      <rect class="brick-a" x="1105" y="336" width="95" height="83"/>

      <rect class="brick-a" x="0" y="425" width="218" height="91"/>
      <rect class="brick-d" x="224" y="425" width="244" height="91"/>
      <rect class="brick-a" x="474" y="425" width="243" height="91"/>
      <rect class="brick-a" x="723" y="425" width="247" height="91"/>
      <rect class="brick-b" x="976" y="425" width="224" height="91"/>

      <rect class="brick-a" x="0" y="522" width="97" height="83"/>
      <rect class="brick-a" x="103" y="522" width="244" height="83"/>
      <rect class="brick-a" x="353" y="522" width="247" height="83"/>
      <rect class="brick-a" x="606" y="522" width="243" height="83"/>
      <rect class="brick-a" x="855" y="522" width="244" height="83"/>
      <rect class="brick-a" x="1105" y="522" width="95" height="83"/>

      <rect class="brick-a" x="0" y="611" width="218" height="92"/>
      <rect class="brick-b" x="224" y="611" width="244" height="92"/>
      <rect class="brick-a" x="474" y="611" width="243" height="92"/>
      <rect class="brick-c" x="723" y="611" width="247" height="92"/>
      <rect class="brick-d" x="976" y="611" width="224" height="92"/>

      <rect class="brick-a" x="0" y="709" width="97" height="85"/>
      <rect class="brick-a" x="103" y="709" width="244" height="85"/>
      <rect class="brick-a" x="353" y="709" width="247" height="85"/>
      <rect class="brick-a" x="606" y="709" width="243" height="85"/>
      <rect class="brick-a" x="855" y="709" width="244" height="85"/>
      <rect class="brick-d" x="1105" y="709" width="95" height="85"/>
    </g>
    <rect class="ground" x="0" y="796" width="1200" height="53"/>
    <rect class="ground-edge" x="0" y="796" width="1200" height="5"/>
  </svg>

  <div class="child-art" role="img" aria-label="Happy child standing on top of the brick wall, arms raised, holding a large completed puzzle"></div>
  <div class="ground-puzzle left" role="img" aria-label="Unfinished puzzle pieces lying on the grass"></div>
  <div class="ground-puzzle right" role="img" aria-label="Unfinished puzzle pieces lying on the grass"></div>

  <header class="masthead">
    <h1 class="title">Speech/Language Therapy</h1>
    <p class="subtitle">The Foundation for Communication</p>
    <p class="headline">SUCCESS</p>
  </header>

  <p class="brick-word" style="left:0;top:252px;width:218px;height:78px">Receptive Language</p>
  <p class="brick-word" style="left:474px;top:252px;width:243px;height:78px">Pragmatics</p>
  <p class="brick-word" style="left:976px;top:252px;width:224px;height:78px">Expressive Language</p>

  <p class="brick-word" style="left:103px;top:336px;width:244px;height:83px">Cognitive</p>
  <p class="brick-word" style="left:606px;top:336px;width:243px;height:83px">Social Language</p>
  <p class="brick-word" style="left:855px;top:336px;width:244px;height:83px">Autism</p>

  <p class="brick-word" style="left:0;top:425px;width:218px;height:91px">Sensory</p>
  <p class="brick-word" style="left:474px;top:425px;width:243px;height:91px">Auditory Processing</p>
  <p class="brick-word" style="left:976px;top:425px;width:224px;height:91px">TeleTherapy</p>

  <p class="brick-word" style="left:103px;top:522px;width:244px;height:83px">Screening</p>
  <p class="brick-word" style="left:353px;top:522px;width:247px;height:83px">Evaluation</p>
  <p class="brick-word" style="left:855px;top:522px;width:244px;height:83px">Developmental Delay</p>

  <p class="brick-word" style="left:224px;top:611px;width:244px;height:92px">Goals</p>
  <p class="brick-word" style="left:474px;top:611px;width:243px;height:92px">ASD</p>
  <p class="brick-word" style="left:723px;top:611px;width:247px;height:92px">Family Involvement</p>

  <p class="brick-word" style="left:103px;top:709px;width:244px;height:85px">Environmental Communication</p>
  <p class="brick-word" style="left:353px;top:709px;width:247px;height:85px">Articulation</p>
  <p class="brick-word" style="left:606px;top:709px;width:243px;height:85px">Mirror Neurons</p>
</div>
</body>
</html>
```